Modern e-Commerce Website for new tea company

We need a web design for a new company called "leaf meadows" based in the UK. We are operating in the food / retailing industry. We are an online retailer of organic Darjeeling Tea (Black and Green Tea) - our clients are end-customers within the UK.

We are looking for a coded wordpress webdesign for a landing page, a potential second page and an online shop.

Target Market(s)

End-customers of tea within the UK

Industry/Entity Type

E-Commerce

Coding

Coded - Design and coding required

Number of Pages Required

3 page

Font styles to use
Other font styles liked:
• Helvetica Neue

Requirements
Must have
• Design expectations:
• We are looking for a very professional looking website. A website that shows the type quality we put into preparing our tea every day. Overall theme of the website should be simplie and clean (white, green). But pictures of tea should be more colourful. Graphics like buttons, text, etc. should be simple, shouldn't stick out too much. Also, don't forget that this website is for people buying tea, so the design should make tea look more appetising.
• Websites that inspire us are:
• https://www.brovelle.co.uk/about-brovelle/brovelle-teas/darjeeling
• - nice colours, icons, graphics
• https://www.quenpo.com/
• - well designed, simple
• https://www.dulvo.com/
• - simple, clear sections for each point
• How we want each page to be designed
• 1) Landing Page (one-page)
• - sticky menu (header)
• - section 1: slider with pictures of our products
• - section 2: product overview with product pictures
• - section 3: advantages of our products
• - section 4: how our concept works
• - contact us
• - footer (twitter, fb, instagram, disclaimer)
• 2) Second page
• 3) Shop
• Our current site is: http://marquin.sitebarn.pw/wp/
Nice to have
• What to avoid
• We want this website to consist of soft colours, so we DON'T want colours that are too hard on the eyes and are "highlighter" like colours. We don't want this website to look too "cartoon like" or too "childish". We are going for a sophisticated, high class look.

```html
<!DOCTYPE html>
<html lang="en">
<head>
<meta charset="utf-8">
<title>Hillcrest Leaf – Darjeeling Tea</title>
<link rel="stylesheet" href="https://fonts.googleapis.com/css2?family=Open+Sans:wght@400;700;800&family=Roboto:wght@300;400;500;700&family=Roboto+Condensed:wght@400;700&display=swap">
<style>
:root{
  --green:#4a9a10;
  --green-dark:#3a8a0c;
  --footer:#3f9c12;
  --ink:#1a1a1a;
  --grey:#666;
  --line:#d9d9d9;
  --field:#efefef;
}
*{box-sizing:border-box;margin:0;padding:0}
html,body{width:1200px;height:4054px;overflow:hidden;background:#fff}
body{position:relative;font-family:"Roboto",Arial,sans-serif;color:var(--ink)}
.abs{position:absolute}
.green{color:var(--green)}

/* header */
.site-header{position:absolute;left:0;top:0;width:1200px;height:208px;background:#fff}
.phone{left:78px;top:44px;font:700 30px "Roboto",sans-serif;color:var(--green);display:flex;align-items:center;gap:16px}
.brand{left:500px;top:30px;width:200px;text-align:center}
.brand-dot{width:56px;height:56px;border-radius:50%;background:#2b2b2b;margin:0 auto 10px}
.brand-name{font:700 13px "Open Sans",sans-serif;letter-spacing:1px;color:#222;text-transform:uppercase}
.account{right:78px;top:52px;font:400 16px "Roboto",sans-serif;color:#555;display:flex;gap:18px;align-items:center}
.account span.sep{width:1px;height:22px;background:#ccc}
.nav-rule{left:78px;width:1044px;height:4px;background:#e6e6e6}
.main-nav{left:78px;top:160px;display:flex;font:400 17px "Roboto Condensed",sans-serif;color:#333;text-transform:uppercase}
.main-nav a{color:inherit;text-decoration:none;margin-right:68px}
.main-nav a:first-child{margin-right:62px}

/* hero */
.hero{left:0;top:208px;width:1200px;height:719px;background:linear-gradient(180deg,#e9b79d 0%,#d7a27a 14%,#8a9a3a 34%,#4f7d1c 60%,#3b6a14 100%)}
.hero h1{position:absolute;left:81px;top:97px;font:700 44px/1.24 "Open Sans",sans-serif;color:#111;text-transform:uppercase;letter-spacing:.5px}

/* welcome + products */
.section-title{width:1200px;text-align:center;font:400 41px "Roboto",sans-serif;color:#111}
.welcome-sub{width:1200px;text-align:center;font:400 16px/27px "Open Sans",sans-serif;color:#666}
.product{width:321px;text-align:center}
.product.featured{border:2px solid #ddd;box-shadow:0 2px 8px rgba(0,0,0,.15);height:362px}
.product-img{width:150px;height:150px;margin:0 auto;border-radius:50%;background:radial-gradient(circle,#7a4a22 0%,#4a2a10 55%,rgba(255,255,255,0) 72%)}
.product h3{font:400 32px "Roboto",sans-serif;margin-top:40px;color:#222}
.price{font:400 20px "Roboto",sans-serif;color:#777;margin-top:6px}
.btn-outline{display:inline-block;width:173px;height:46px;line-height:42px;border:2px solid #888;border-radius:24px;font:400 18px "Roboto",sans-serif;color:#444;text-transform:uppercase;margin-top:20px}

/* about */
.about{left:0;top:1676px;width:1200px;height:473px;background:linear-gradient(90deg,#fff 0%,#f6f6f1 50%,#eef0e4 100%)}
.about-img{position:absolute;right:0;top:0;width:551px;height:473px;background:radial-gradient(circle at 60% 62%,#d79a22 0%,#c77e10 22%,#8aa35a 48%,#dfe6d2 80%)}
.about-brand{position:absolute;left:78px;top:54px;display:flex;align-items:center;gap:16px}
.about-brand .brand-dot{margin:0;width:70px;height:70px}
.about h2{position:absolute;left:78px;top:206px;font:400 48px "Roboto",sans-serif;color:#111}
.about p{position:absolute;left:78px;top:282px;width:560px;font:400 16px/26px "Open Sans",sans-serif;color:#333}
.btn-solid{position:absolute;left:78px;top:378px;width:249px;height:56px;background:var(--green);color:#fff;font:700 21px/56px "Roboto Condensed",sans-serif;text-align:center;text-transform:uppercase}

/* advantages */
.advantages{left:0;top:2149px;width:1200px;height:622px;background:linear-gradient(180deg,#6a8f2e 0%,#557f20 40%,#44701a 100%)}
.adv-kicker{top:70px;width:1200px;text-align:center;font:400 16px "Roboto",sans-serif;color:#fff;text-transform:uppercase}
.adv-title{top:92px;width:1200px;text-align:center;font:400 42px "Roboto",sans-serif;color:#fff;text-transform:uppercase;letter-spacing:1px}
.adv-cup{left:462px;top:200px;width:276px;height:340px;border-radius:50%;background:radial-gradient(ellipse,#d8e2b0 0%,#c0cf8e 40%,#dfe8d0 60%,rgba(255,255,255,0) 71%)}
.adv-icon{width:116px;height:116px;border-radius:50%;background:#fff;display:flex;align-items:center;justify-content:center}
.adv-text{width:230px;color:#fff;z-index:2}
.adv-text h4{font:700 22px "Roboto Condensed",sans-serif;text-transform:uppercase}
.adv-text p{font:400 14px/22px "Open Sans",sans-serif;color:#eef3e5;margin-top:4px}
.adv-text.right{text-align:right}
.adv-rule{height:2px;background:rgba(255,255,255,.55)}

/* concept */
.concept-title{top:2806px;width:1200px;text-align:center;font:400 42px "Roboto",sans-serif;color:var(--green);text-transform:uppercase}
.step{width:270px;text-align:center}
.step-icon{width:124px;height:124px;border:2px solid var(--green);border-radius:50%;margin:0 auto;display:flex;align-items:center;justify-content:center}
.step h4{font:500 24px "Roboto",sans-serif;margin-top:20px;color:#111}
.step p{font:400 15px/26px "Open Sans",sans-serif;color:#444;margin-top:6px;padding:0 28px}

/* contact */
.contact{left:0;top:3217px;width:1200px;height:446px;background:linear-gradient(180deg,#dfe3e6 0%,#c8d0d2 30%,#8aa36a 62%,#5f8a2e 100%)}
.contact h2{position:absolute;top:44px;width:1200px;text-align:center;font:400 42px "Roboto",sans-serif;color:#1e3a08;text-transform:uppercase}
.contact .lead{position:absolute;top:116px;width:1200px;text-align:center;font:400 16px/24px "Open Sans",sans-serif;color:#333}
.field{position:absolute;background:var(--field);font:400 13px "Open Sans",sans-serif;color:#888;padding:18px 22px}
.submit{position:absolute;left:462px;top:332px;width:622px;height:60px;background:var(--green);color:#fff;font:400 26px/60px "Roboto Condensed",sans-serif;text-align:center;text-transform:uppercase}

/* footer */
.site-footer{left:0;top:3663px;width:1200px;height:391px;background:var(--footer);color:#fff}
.footer-col{position:absolute;top:0}
.footer-col h5{position:absolute;top:90px;white-space:nowrap;font:400 24px "Roboto",sans-serif;color:#fff}
.footer-brand{position:absolute;left:78px;top:36px;display:flex;align-items:center;gap:14px}
.footer-brand .brand-dot{margin:0;width:76px;height:76px}
.footer-brand .brand-name{color:#111}
.footer-about{position:absolute;left:78px;top:150px;width:240px;font:400 16px/26px "Open Sans",sans-serif}
.read-more{position:absolute;left:78px;top:278px;font:700 15px "Open Sans",sans-serif;color:#111;text-decoration:underline;text-transform:uppercase}
.links{position:absolute;left:357px;top:140px;list-style:none;font:400 16px/27px "Open Sans",sans-serif}
.nl-field{position:absolute;left:622px;width:236px;height:38px;border:1px solid #fff;font:400 15px/36px "Open Sans",sans-serif;padding-left:10px;color:#fff}
.nl-btn{position:absolute;left:622px;top:246px;width:146px;height:44px;background:#5fbf18;font:500 18px/44px "Roboto",sans-serif;text-align:center;text-transform:uppercase}
.contact-list{position:absolute;left:892px;top:140px;width:260px;list-style:none;font:400 17px/30px "Open Sans",sans-serif}
.contact-list li{display:flex;gap:16px;margin-bottom:10px}
.contact-list svg{flex:none;margin-top:6px}
.footer-rule{position:absolute;left:78px;top:343px;width:1044px;height:1px;background:rgba(255,255,255,.6)}
.copyright{position:absolute;top:362px;width:1200px;text-align:center;font:400 15px "Open Sans",sans-serif}
.copyright b{color:#123a00}
</style>
</head>
<body>

<header class="site-header">
  <div class="abs phone">
    <svg width="26" height="26" viewBox="0 0 24 24"><path fill="currentColor" d="M6.6 10.8a15.1 15.1 0 0 0 6.6 6.6l2.2-2.2c.3-.3.7-.4 1-.2 1.1.4 2.3.6 3.6.6.6 0 1 .4 1 1V20c0 .6-.4 1-1 1A17 17 0 0 1 3 4c0-.6.4-1 1-1h3.5c.6 0 1 .4 1 1 0 1.3.2 2.5.6 3.6.1.3 0 .7-.2 1z"/></svg>
    +1 123 456 789
  </div>
  <div class="abs brand">
    <div class="brand-dot"></div>
    <div class="brand-name">Hillcrest Leaf</div>
  </div>
  <div class="abs account">
    <span>&#8618; Login</span><span class="sep"></span><span>&#128722; My Cart</span>
  </div>
  <div class="abs nav-rule" style="top:136px"></div>
  <nav class="abs main-nav">
    <a href="#">Home</a><a href="#">Products</a><a href="#">Overview</a><a href="#">Advantages</a><a href="#">Concept</a><a href="#">Contact</a>
  </nav>
  <div class="abs nav-rule" style="top:203px;height:2px"></div>
</header>

<section class="abs hero" role="img" aria-label="Terraced tea garden on rolling hills at sunrise">
  <h1>Tired of paying &nbsp;outrageous<br>prices for Darjeeling teas?<br>We fixed that for you.</h1>
</section>

<h2 class="abs section-title" style="top:976px">Welcome To <span class="green">Hillcrest Leaf</span></h2>
<p class="abs welcome-sub" style="top:1040px">Looking for the world's most renowned tea at unbeatable low prices?<br>Available for limited time only!</p>
<h2 class="abs section-title" style="top:1132px;font-size:40px">Featured <span class="green">Products</span></h2>

<div class="abs product" style="left:78px;top:1214px">
  <div class="product-img" style="margin-top:26px" role="img" aria-label="Loose leaf black tea in a wooden scoop"></div>
  <h3>First Flush 2016</h3>
  <div class="price">£19.99 (for 500g)</div>
  <div class="btn-outline">Order Now</div>
</div>
<div class="abs product featured" style="left:441px;top:1214px">
  <div class="product-img" style="margin-top:24px" role="img" aria-label="Cup of tea beside loose tea leaves"></div>
  <h3 style="margin-top:38px">Second Flush 2016</h3>
  <div class="price">£19.99 (for 500g)</div>
  <div class="btn-outline">Order Now</div>
</div>
<div class="abs product" style="left:800px;top:1214px">
  <div class="product-img" style="margin-top:26px;background:radial-gradient(circle,#d99a2a 0%,#a8681a 45%,#7aa044 60%,rgba(255,255,255,0) 72%)" role="img" aria-label="Glass cup of green tea with fresh leaves"></div>
  <h3>Green Tea</h3>
  <div class="price">£14.99 (for 500g)</div>
  <div class="btn-outline">Order Now</div>
</div>

<section class="abs about">
  <div class="about-img" role="img" aria-label="Glass cup of golden tea with fresh herbs"></div>
  <div class="about-brand"><div class="brand-dot"></div><div class="brand-name">Hillcrest Leaf</div></div>
  <h2>Lorem Ipsum is simply dummy.</h2>
  <p>Lorem Ipsum has been the industry's standard dummy text ever since the 1500s, when an unknown printer took a galley of type and scrambled it to make a type specimen book.</p>
  <div class="btn-solid">View All Products</div>
</section>

<section class="abs advantages" role="img" aria-label="Green tea plantation background">
  <div class="abs adv-kicker">What we do</div>
  <div class="abs adv-title">Our Advantages</div>
  <div class="abs adv-cup" role="img" aria-label="Glass cup of green tea on a saucer with a leaf"></div>

  <div class="abs adv-rule" style="left:130px;top:306px;width:320px"></div>
  <div class="abs adv-rule" style="left:750px;top:306px;width:320px"></div>
  <div class="abs adv-rule" style="left:130px;top:520px;width:320px"></div>
  <div class="abs adv-rule" style="left:750px;top:520px;width:320px"></div>

  <div class="abs adv-icon" style="left:72px;top:158px">
    <svg width="56" height="56" viewBox="0 0 24 24" fill="#4a4a4a"><circle cx="12" cy="9" r="6"/><path d="M8 14l-2 8 4-2 2 2 1-7zM16 14l2 8-4-2-2 2-1-7z"/><path fill="#fff" d="M12 5.5l1 2.1 2.3.3-1.7 1.6.4 2.3-2-1.1-2 1.1.4-2.3-1.7-1.6 2.3-.3z"/></svg>
  </div>
  <div class="abs adv-text" style="left:212px;top:180px"><h4>Highest Quality</h4><p>FTGFOP-1. Tasted by one of UK's most renowned tea tasters.</p></div>

  <div class="abs adv-icon" style="left:1012px;top:158px">
    <svg width="56" height="56" viewBox="0 0 24 24" fill="none" stroke="#4a4a4a" stroke-width="2.2"><circle cx="10" cy="10" r="6.5"/><path d="M15 15l6 6" stroke-linecap="round"/></svg>
  </div>
  <div class="abs adv-text right" style="left:758px;top:180px"><h4>Full Transparency</h4><p>We did everything to eliminate all unnecessary costs in order to</p></div>

  <div class="abs adv-icon" style="left:72px;top:374px">
    <svg width="56" height="56" viewBox="0 0 24 24" fill="#4a4a4a"><ellipse cx="12" cy="6" rx="8" ry="3"/><path d="M4 9c0 1.7 3.6 3 8 3s8-1.3 8-3v2.5c0 1.7-3.6 3-8 3s-8-1.3-8-3zM4 14c0 1.7 3.6 3 8 3s8-1.3 8-3v2.5c0 1.7-3.6 3-8 3s-8-1.3-8-3z"/></svg>
  </div>
  <div class="abs adv-text" style="left:212px;top:396px"><h4>Low Price</h4><p>Look up pesticide analysis results of your tea and ...</p></div>

  <div class="abs adv-icon" style="left:1012px;top:374px">
    <svg width="56" height="56" viewBox="0 0 24 24" fill="#4a4a4a"><path d="M20 3C9 3 4 9 4 16c0 1.5.3 3 .8 4l1.4-.7C9 13 13 10 17 8c-4 3-7.5 6.5-9.5 12C16 21 21 14 20 3z"/></svg>
  </div>
  <div class="abs adv-text right" style="left:758px;top:396px"><h4>100% Organic</h4><p>All our tea is from certified organic production. Inspected by</p></div>
</section>

<h2 class="abs concept-title">Concept</h2>

<svg class="abs" style="left:270px;top:2900px" width="660" height="80" viewBox="0 0 660 80" fill="none" stroke="#111" stroke-width="4" stroke-linecap="round">
  <path d="M20 38c30-22 70-22 98 4"/><path d="M104 30l14 12-18 4"/>
  <path d="M290 60c26-8 40-22 56-40"/><path d="M330 20l16 0-4 16"/>
  <path d="M560 38c30-22 70-22 98 4"/><path d="M644 30l14 12-18 4"/>
</svg>

<div class="abs step" style="left:60px;top:2879px">
  <div class="step-icon"><svg width="54" height="54" viewBox="0 0 24 24" fill="none" stroke="#4a9a10" stroke-width="2.6" stroke-linecap="round"><path d="M5 19L19 5M12 5h7v7M5 12v7h7"/></svg></div>
  <h4>Large Packages</h4>
  <p>By using large packets (500g, 1000g), we can save on packaging, labeling and handling costs.</p>
</div>
<div class="abs step" style="left:330px;top:2879px">
  <div class="step-icon"><svg width="54" height="54" viewBox="0 0 24 24" fill="none" stroke="#4a9a10" stroke-width="2.6" stroke-linecap="round" stroke-linejoin="round"><path d="M3 12h18M7 8l-4 4 4 4M17 8l4 4-4 4"/></svg></div>
  <h4>Direct Trade</h4>
  <p>We cut all middlemen and buy directly from the leaf meadows in Darjeeling.</p>
</div>
<div class="abs step" style="left:600px;top:2879px">
  <div class="step-icon"><svg width="58" height="58" viewBox="0 0 24 24" fill="none" stroke="#4a9a10" stroke-width="3.4" stroke-linecap="round" stroke-linejoin="round"><path d="M4 12.5l5 5L20 6.5"/></svg></div>
  <h4>Simplicity</h4>
  <p>We only sell 100% organic high grad FTGFOP-1 darjeeling tea to reduce costs. Nothing else.</p>
</div>
<div class="abs step" style="left:870px;top:2879px">
  <div class="step-icon"><svg width="52" height="52" viewBox="0 0 24 24" fill="#4a9a10"><path d="M3 5h18v16H3z" fill="none" stroke="#4a9a10" stroke-width="2"/><path d="M3 5h18v4H3zM7 2h2v5H7zM15 2h2v5h-2zM6 11h3v3H6zM10.5 11h3v3h-3zM15 11h3v3h-3zM6 15.5h3v3H6zM10.5 15.5h3v3h-3zM15 15.5h3v3h-3z"/></svg></div>
  <h4>One Year's Supply</h4>
  <p>Tea stores well for long periods of time. Therefore many of our customers buy their year's supply at a time. This reduces shipping costs.</p>
</div>

<section class="abs contact" role="img" aria-label="Green hills under a cloudy sky">
  <h2>Contect</h2>
  <p class="lead">Do you still have any questions?<br>One way to get in touch with us is to fill out the following form.</p>
  <div class="field" style="left:116px;top:189px;width:333px;height:60px">Name</div>
  <div class="field" style="left:116px;top:264px;width:333px;height:58px">E - Mail</div>
  <div class="field" style="left:116px;top:332px;width:333px;height:60px">Phone</div>
  <div class="field" style="left:462px;top:189px;width:622px;height:135px;padding-top:14px">Message</div>
  <div class="submit">Submit</div>
</section>

<footer class="abs site-footer">
  <div class="footer-brand"><div class="brand-dot"></div><div class="brand-name">Hillcrest Leaf</div></div>
  <p class="footer-about">Lorem Ipsum is simply<br>dummy text of the printing<br>and typesetting industry.<br>Lorem Ipsum has been.</p>
  <a class="read-more">Read More</a>

  <div class="footer-col" style="left:357px"><h5>Useful Links</h5></div>
  <ul class="links"><li>Home</li><li>Products</li><li>Overview</li><li>Advantages</li><li>Concept</li><li>Contact</li></ul>

  <div class="footer-col" style="left:622px"><h5>Newsletter</h5></div>
  <div class="nl-field" style="top:140px">Enter Name</div>
  <div class="nl-field" style="top:192px">Enter Email</div>
  <div class="nl-btn">Subscribe</div>

  <div class="footer-col" style="left:892px"><h5>Get In Touch</h5></div>
  <ul class="contact-list">
    <li><svg width="18" height="22" viewBox="0 0 24 24" fill="#fff"><path d="M12 2a7 7 0 0 0-7 7c0 5 7 13 7 13s7-8 7-13a7 7 0 0 0-7-7zm0 9.5A2.5 2.5 0 1 1 12 6.5a2.5 2.5 0 0 1 0 5z"/></svg><span>Lorem Ipsum is simply dummy text of the printing</span></li>
    <li><svg width="18" height="18" viewBox="0 0 24 24" fill="#fff"><path d="M6.6 10.8a15.1 15.1 0 0 0 6.6 6.6l2.2-2.2c.3-.3.7-.4 1-.2 1.1.4 2.3.6 3.6.6.6 0 1 .4 1 1V20c0 .6-.4 1-1 1A17 17 0 0 1 3 4c0-.6.4-1 1-1h3.5c.6 0 1 .4 1 1 0 1.3.2 2.5.6 3.6.1.3 0 .7-.2 1z"/></svg><span>+1 123 456 789</span></li>
    <li><svg width="20" height="16" viewBox="0 0 24 18" fill="none" stroke="#fff" stroke-width="2"><rect x="1" y="1" width="22" height="16"/><path d="M1 1l11 9 11-9"/></svg><span>info@hillcrestleaf.co.uk</span></li>
  </ul>

  <div class="footer-rule"></div>
  <p class="copyright">© <b>Hillcrest Leaf</b> - 2016. All Rights Reserved.</p>
</footer>

</body>
</html>
```